Sales sheet for printing and embroidery apparel items - Copper Fern Prints

I would like a one page flyer or sales sheet that I would use as a template to send different images of apparel we produce. I have attached examples of layouts I like.
- Ideally, it would have space for 3-5 items.
- I would like it one page only - not a folding flyer.
- Our companies name is Copper Fern Prints.
- This will be used for many different products and markets so I don't need wording/copy. You can use wording from the 7Q7 or K81 flyer.

Colors
0054AA
0677BA
7BADD7
CADEEF
E8F1F8
00AB8E
00BBA5
67D7C9
C6EFE9
E9F9F6
FFC000
F8CF3A
FAE287
FDF2CF
FEFAEE

Requirements
Must have
• Places for between 3 and 5 images of apparel (t-shirts, hats etc)

```html
<!DOCTYPE html>
<html lang="en">
<head>
<meta charset="utf-8">
<title>Copper Fern Prints – Sales Sheets</title>
<link href="https://fonts.googleapis.com/css2?family=Roboto:ital,wght@0,400;0,500;0,700;0,900;1,700;1,900&family=Roboto+Condensed:wght@700&display=swap" rel="stylesheet">
<style>
:root{
  --backdrop:#7f7e8a;
  --navy:#0b2547;
  --blue:#1570b3;
  --blue-mid:#0f5c9c;
  --ink:#2b2d5e;
  --orange:#e0552b;
  --yellow:#f6c318;
  --paper:#f4f2f0;
  --paper-low:#e3e1df;
  --white:#ffffff;
}
*{margin:0;padding:0;box-sizing:border-box}
html,body{width:1200px;height:2619px;overflow:hidden;background:var(--backdrop);font-family:"Roboto",Arial,sans-serif;color:var(--ink)}
.sheet{position:absolute;left:178px;width:828px;height:1071px;overflow:hidden;background:linear-gradient(180deg,var(--white) 40%,var(--paper) 70%,var(--paper-low) 100%)}
.sheet--kit{top:187px}
.sheet--order{top:1323px}
.sheet svg.backdrop{position:absolute;left:0;top:0;width:828px;height:1071px}
.abs{position:absolute}
.center{left:0;width:828px;text-align:center}

/* header – kit */
.brand-title{left:40px;top:90px;width:640px;font-family:"Roboto",Arial,sans-serif;font-weight:900;font-size:82px;line-height:1;color:var(--white);text-align:center}
.badge{left:690px;top:193px;width:87px;height:75px;background:var(--orange)}
.est{left:672px;top:276px;width:124px;text-align:center;color:var(--white);font-weight:700;font-size:20px}

.section-title{font-weight:900;font-style:italic;font-size:46px;letter-spacing:-1px}
.section-title .hot{color:var(--orange)}
.section-title .gold{color:var(--yellow)}
.meta{font-weight:700;font-size:20px;color:var(--ink)}
.meta .key{color:var(--orange)}

.shirt{top:570px;width:230px;height:228px;border-radius:30px 30px 10px 10px}
.shirt--olive{left:40px;background:#5b5636}
.shirt--black{left:298px;background:#0a0a0a}
.shirt--navy{left:553px;background:#2d2f86}

.warning{left:40px;width:748px;text-align:center;font-weight:500;font-size:18px;line-height:23px}
.warning .key{color:var(--orange);font-weight:700}

.contents{left:42px;width:746px;height:31px;background:var(--orange);border-top:4px solid var(--yellow);color:var(--white);font-weight:700;font-size:16px;display:flex;align-items:center;padding-left:16px;gap:12px}
.contents .label{margin-right:8px}
.contents .num{display:inline-flex;width:18px;height:18px;border-radius:50%;background:var(--white);color:var(--orange);font-size:12px;align-items:center;justify-content:center;margin-right:5px}
.invite{font-size:19px;font-weight:400}
.contact{left:50px;display:flex;align-items:center;gap:12px;font-weight:700;font-size:19px}
.contact .item{display:flex;align-items:center;gap:6px}
.contact svg{width:24px;height:24px}

/* header – order */
.order-logo{left:74px;top:38px;width:114px;height:90px;background:var(--orange);border:4px solid var(--white)}
.order-brand{left:40px;top:140px;width:180px;text-align:center;color:var(--white);font-family:"Roboto Condensed",Arial,sans-serif;font-weight:700;font-size:26px;line-height:1}
.order-title{left:258px;top:34px;color:var(--white);font-weight:900;font-style:italic;font-size:40px}
.order-sub{left:258px;top:82px;color:var(--yellow);font-weight:700;font-style:italic;font-size:29px}
.order-about{left:258px;top:138px;width:520px;color:var(--white);font-weight:700;font-size:15.5px;line-height:20px}

.photo{top:477px;width:232px;height:158px;padding:5px;background:linear-gradient(180deg,var(--yellow),var(--orange))}
.photo div{width:100%;height:100%;background:radial-gradient(ellipse at center,#3c3f48 0%,#1b1d22 80%)}
.photo--a{left:52px}
.photo--b{left:302px}
.photo--c{left:552px}

.offer-head{font-weight:700;font-size:18px;color:var(--orange)}
.offer-body{left:60px;width:708px;text-align:center;font-size:18.5px;line-height:23px}
.fine{left:40px;width:748px;text-align:center;font-size:15.5px;line-height:19.5px}
</style>
</head>
<body>

<section class="sheet sheet--kit">
  <svg class="backdrop" viewBox="0 0 828 1071" aria-hidden="true">
    <defs>
      <linearGradient id="headBlue" x1="0" y1="0" x2="0" y2="1">
        <stop offset="0" stop-color="#0b2547"/><stop offset="0.45" stop-color="#0f5c9c"/><stop offset="1" stop-color="#1673b4"/>
      </linearGradient>
      <linearGradient id="flare" x1="0" y1="0" x2="1" y2="0">
        <stop offset="0" stop-color="#e0552b"/><stop offset="1" stop-color="#f6c318"/>
      </linearGradient>
    </defs>
    <path d="M0 0H828V420C760 395 700 370 640 395C560 430 500 385 420 420C330 455 270 410 190 450C120 480 60 470 0 495Z" fill="url(#headBlue)"/>
    <path d="M680 370C720 330 760 345 790 320C805 335 815 320 828 325V420C790 395 740 390 680 370Z" fill="url(#flare)"/>
    <path d="M390 1071C470 1045 540 1050 610 1015C690 980 760 975 828 925V1071Z" fill="url(#headBlue)"/>
  </svg>

  <h1 class="abs brand-title">Copper Fern Prints</h1>
  <div class="abs badge"></div>
  <p class="abs est">Est. 1979</p>

  <h2 class="abs center section-title" style="top:432px"><span class="hot">Sample</span> <span class="gold">Merch Kit</span></h2>
  <p class="abs center meta" style="top:517px"><span class="key">MODEL:</span> CFP SHOP T-SHIRTS • <span class="key">SERIES:</span> SUMMER/FALL 2026 COLLECTION</p>

  <div class="abs shirt shirt--olive" role="img" aria-label="Olive t-shirt with a printed vintage truck graphic"></div>
  <div class="abs shirt shirt--black" role="img" aria-label="Black t-shirt with a printed off-road truck graphic"></div>
  <div class="abs shirt shirt--navy" role="img" aria-label="Navy t-shirt with a printed classic car sunset graphic"></div>

  <p class="abs warning" style="top:822px"><span class="key">WARNING:</span> These shirts may cause increased shop morale, envy from competitors, and a high volume of customer demand.</p>

  <div class="abs contents" style="top:883px">
    <span class="label">MERCH KIT CONTENTS:</span>
    <span><span class="num">1</span>Custom Shop T-shirt</span>
    <span><span class="num">2</span>Additional Sample Shirt</span>
    <span><span class="num">3</span>CFP Ink Pen</span>
  </div>

  <p class="abs center invite" style="top:935px">We'd love to work with you! Contact Marcus Delane to start your next shirt order today.</p>
  <div class="abs contact" style="top:972px">
    <span class="item"><svg viewBox="0 0 24 24"><circle cx="12" cy="12" r="12" fill="#e0552b"/><path d="M8 6l2 0 1 3-1.5 1.2a8 8 0 0 0 4.3 4.3L15 13l3 1v2c0 1-1 2-2 2A10 10 0 0 1 6 8c0-1 1-2 2-2z" fill="#fff"/></svg>555-018-2746</span>
    <span class="item"><svg viewBox="0 0 24 24"><circle cx="12" cy="12" r="12" fill="#e0552b"/><rect x="6" y="8" width="12" height="9" rx="1" fill="#fff"/><path d="M6.5 8.5l5.5 4.5 5.5-4.5" stroke="#e0552b" stroke-width="1.3" fill="none"/></svg>marcus@cfpshirts.com</span>
    <span class="item"><svg viewBox="0 0 24 24"><circle cx="12" cy="12" r="12" fill="#e0552b"/><path d="M8 7l9 4-4 1.3 3 3.5-1.5 1.2-3-3.5L9 16z" fill="#fff"/></svg>cfpshirts.com</span>
  </div>
</section>

<section class="sheet sheet--order">
  <svg class="backdrop" viewBox="0 0 828 1071" aria-hidden="true">
    <path d="M0 0H828V290C760 270 700 250 640 270C560 305 500 260 420 290C330 320 270 290 190 320C120 345 60 345 0 370Z" fill="url(#headBlue)"/>
    <path d="M680 240C720 205 760 220 790 195C805 210 815 195 828 200V290C790 270 740 260 680 240Z" fill="url(#flare)"/>
    <path d="M390 1071C470 1045 540 1050 610 1015C690 980 760 975 828 925V1071Z" fill="url(#headBlue)"/>
  </svg>

  <div class="abs order-logo"></div>
  <p class="abs order-brand">COPPER FERN PRINTS</p>
  <h1 class="abs order-title">HOW TO START AN ORDER</h1>
  <p class="abs order-sub">Creating T-shirts is quick and easy</p>
  <p class="abs order-about">Copper Fern Prints is a second-generation screen printing company in Harlow Falls, VA. For over 45 years, we've specialized in high-quality custom apparel and merchandise.</p>

  <h2 class="abs center section-title" style="top:362px"><span class="hot">Premium</span> <span class="gold">Embroidery</span></h2>
  <p class="abs center meta" style="top:431px">STICH WITH IMPACT</p>

  <div class="abs photo photo--a"><div role="img" aria-label="Photo of a cream and black cap with embroidered script lettering"></div></div>
  <div class="abs photo photo--b"><div role="img" aria-label="Photo of two embroidered caps, one black and one green and cream"></div></div>
  <div class="abs photo photo--c"><div role="img" aria-label="Photo of a tan cap with colorful embroidered script lettering"></div></div>

  <p class="abs center offer-head" style="top:685px">WE OFFER:</p>
  <p class="abs offer-body" style="top:707px">• Art Design • Free Shipping • We Pay ALL Royalties to the Movement Many Options of Shirt Styles and Colors</p>

  <p class="abs center offer-head" style="top:775px">THE FINE PRINT:</p>
  <p class="abs fine" style="top:796px">Please send high-resolution images. When sending additional logos, please send vector images.<br>Note that our shop minimum is 24 pieces for one-color prints &amp; 100 pieces for full-color screen print.<br>We also promise accurate, quality work.</p>

  <div class="abs contents" style="top:883px">
    <span class="label">MERCH KIT CONTENTS:</span>
    <span><span class="num">1</span>Custom Shop T-shirt</span>
    <span><span class="num">2</span>Additional Sample Shirt</span>
    <span><span class="num">3</span>CFP Ink Pen</span>
  </div>

  <p class="abs center invite" style="top:942px">We'd love to work with you! Contact Marcus Delane to start your next shirt order today.</p>
  <div class="abs contact" style="top:980px">
    <span class="item"><svg viewBox="0 0 24 24"><circle cx="12" cy="12" r="12" fill="#e0552b"/><path d="M8 6l2 0 1 3-1.5 1.2a8 8 0 0 0 4.3 4.3L15 13l3 1v2c0 1-1 2-2 2A10 10 0 0 1 6 8c0-1 1-2 2-2z" fill="#fff"/></svg>555-018-2746</span>
    <span class="item"><svg viewBox="0 0 24 24"><circle cx="12" cy="12" r="12" fill="#e0552b"/><rect x="6" y="8" width="12" height="9" rx="1" fill="#fff"/><path d="M6.5 8.5l5.5 4.5 5.5-4.5" stroke="#e0552b" stroke-width="1.3" fill="none"/></svg>marcus@cfpshirts.com</span>
    <span class="item"><svg viewBox="0 0 24 24"><circle cx="12" cy="12" r="12" fill="#e0552b"/><path d="M8 7l9 4-4 1.3 3 3.5-1.5 1.2-3-3.5L9 16z" fill="#fff"/></svg>cfpshirts.com</span>
  </div>
</section>

</body>
</html>
```